Wordpress Design Project

Moraby Pathways is a social entrepreneurship program that organizes and leads development projects in and educational expeditions to Guatemala in order to promote economic development.

We want our website to convey our sustainable business model with colors (greens, yellows, organges,like our logo, etc.) that match our logo, which will be integrated throughout the site, as well as our slogan (Wander, Gather, Reach higher, Come along the Journey).

We want the entire site to appear simple and easy to navigate. We want our name and logo to be featured prominently at the top of our home page as well as our slogan with very large (revolving/changing) photographs featured below or as a background to the page. If possible we would like quotes, testimonials about our programs, or statistics on Guatemala to be printed over these photos.

The first of the sections headings displayed should be eXplore (About Moraby) and underneath will appear our Mission and Philosophy, History, Advisory Board, and Founder information. The second should be eXperience with Our Approach, Our Partners here and abroad, Themed Trips, Pricing and Sample Trips, and the $5 Quest. The third should be eXpect More (Benefits) with Online Store and Past Trips below. The remaining section header should be Request a Proposal.

Target Market(s)

U.S. and Canadian university students and professors and philanthropic or social entrepreneurship organizations

Requirements
Must have
• - include a space for the video on the homepage
- logo, company name and slogan, and large colorful photographs as listed in the description
Nice to have
• http://www.brightloomfund.org/
http://tallcedarproject.org/
Should not have
• -not crowded or overwhelmed with text or visuals

```html
<!DOCTYPE html>
<html lang="en">
<head>
<meta charset="utf-8">
<title>Moraby Pathways</title>
<link href="https://fonts.googleapis.com/css2?family=Open+Sans:wght@400;600;700&family=Arimo:wght@400;700&family=Poppins:wght@600&display=swap" rel="stylesheet">
<style>
:root{
  --green:#2e9b3a;
  --green-dark:#1f7a2a;
  --lime:#b9c81a;
  --lime-bright:#d6e23a;
  --brown:#5a2e12;
  --brown-dark:#3e1e0a;
  --text:#3a3a3a;
  --muted:#666;
  --line:#e2e2e2;
  --grey-btn:#dcdcdc;
  --white:#fff;
  --page-bg:#fbfbf8;
}
*{box-sizing:border-box;margin:0;padding:0}
html,body{width:1200px;height:2357px;overflow:hidden}
body{position:relative;background:var(--white);font-family:"Arimo",Arial,sans-serif;color:var(--text);font-size:12px;line-height:1.45}
.abs{position:absolute}
.content-bg{left:0;top:600px;width:1200px;height:1462px;background:var(--page-bg)}

/* hero */
.hero{left:0;top:0;width:1200px;height:600px;background:linear-gradient(180deg,#cfe0dc 0%,#a9c6c2 30%,#7fa39a 55%,#4f7a4f 80%,#3e6838 100%)}
.hero-shade{left:0;top:0;width:1200px;height:600px;background:linear-gradient(90deg,rgba(255,255,255,.25),rgba(255,255,255,0) 20%,rgba(255,255,255,0) 80%,rgba(255,255,255,.25))}
.logo{left:128px;top:29px;width:172px;height:172px;border-radius:50%;background:var(--white);border:8px solid var(--green);display:flex;align-items:center;justify-content:center;text-align:center}
.logo span{font-family:"Open Sans",sans-serif;font-weight:700;color:var(--green);font-size:22px;line-height:1.1}
.util{left:737px;top:51px;width:334px;height:66px;background:rgba(240,235,205,.9);border-radius:4px}
.util .label{position:absolute;left:22px;top:12px;font-size:11px;color:#777}
.util .social{position:absolute;left:22px;top:30px;display:flex;gap:4px}
.util .social i{display:block;width:20px;height:20px;background:#8a8a7a;border-radius:2px}
.util .links{position:absolute;left:162px;top:8px;font-size:11px;color:#777;white-space:nowrap}
.util .search{position:absolute;left:160px;top:30px;width:162px;height:24px;background:var(--white);border:1px solid #ddd;font-size:11px;color:#999;padding:4px 8px}
.nav{left:305px;top:134px;width:766px;height:37px;background:var(--white);display:flex;align-items:stretch;padding-left:2px}
.nav a{font-family:"Open Sans",sans-serif;font-weight:700;font-size:13px;color:#333;text-decoration:none;padding:0 8px;display:flex;align-items:center;border-right:1px solid #eee}
.nav a.active{background:var(--green);color:var(--white)}
.slogan{left:140px;top:222px;font-family:"Poppins",sans-serif;font-weight:600;font-size:58px;line-height:66px;color:var(--white);letter-spacing:-1px}
.slogan .mid{color:var(--lime-bright)}
.cta{left:146px;top:447px;width:310px;height:53px;background:var(--brown);border-radius:5px;color:var(--lime-bright);font-family:"Poppins",sans-serif;font-weight:600;font-size:21px;display:flex;align-items:center;justify-content:center;gap:12px;box-shadow:0 2px 4px rgba(0,0,0,.4)}
.cta svg{width:22px;height:22px}
.arrow{width:34px;height:34px;border-radius:50%;background:rgba(0,0,0,.35)}
.video{left:566px;top:214px;width:507px;height:343px;background:#1c1c1c}
.video .screen{position:absolute;left:0;top:0;width:100%;height:305px;background:linear-gradient(180deg,#e8ecea 0%,#d7e0d4 55%,#c6d3b8 100%)}
.player{position:absolute;left:0;bottom:0;width:100%;height:34px;background:#1c1c1c}
.player .bar{position:absolute;left:0;top:-4px;width:100%;height:4px;background:#555}
.player .bar i{display:block;width:28%;height:100%;background:#d11}
.player .time{position:absolute;left:84px;top:9px;color:#ddd;font-size:11px}
.player .q{position:absolute;right:60px;top:9px;color:#ddd;font-size:11px}
.player .play{position:absolute;left:16px;top:10px;width:12px;height:14px;border-left:4px solid #ddd;border-right:4px solid #ddd}

/* headings */
.h2{font-family:"Open Sans",sans-serif;font-weight:600;font-size:21px;color:var(--green);display:flex;align-items:center;gap:10px}
.h2 .tag{background:var(--lime);color:var(--white);font-size:12px;padding:2px 10px;font-weight:600;clip-path:polygon(8px 0,100% 0,100% 100%,8px 100%,0 50%)}
.h2.side{color:#333}
.rule{height:1px;background:var(--line)}
.para{font-size:12px;color:var(--text)}

/* tiles */
.tile{width:148px;height:138px;border:2px solid var(--lime);border-radius:4px;background:var(--white);display:flex;flex-direction:column;align-items:center;justify-content:center;gap:12px;text-align:center;font-family:"Open Sans",sans-serif;font-weight:600;font-size:13px;color:var(--lime)}
.tile svg{width:40px;height:40px}
.tile.active{background:var(--lime);color:var(--white);height:150px;border:none;clip-path:polygon(0 0,100% 0,100% 88%,50% 100%,0 88%)}
.bul{width:565px;display:flex;gap:20px;font-size:11.5px}
.bul svg{flex:none;width:16px;height:16px;margin-top:1px}

/* program buttons */
.pbtn{width:302px;height:38px;background:var(--grey-btn);border-radius:3px;display:flex;align-items:center;justify-content:space-between;padding:0 10px 0 14px;font-family:"Open Sans",sans-serif;font-weight:600;font-size:13px;color:#444}
.pbtn i{width:20px;height:20px;border-radius:50%;background:#aaa;position:relative}
.pbtn i::after{content:"";position:absolute;left:8px;top:6px;border-left:6px solid var(--white);border-top:4px solid transparent;border-bottom:4px solid transparent}
.pbtn.active{background:var(--brown);color:var(--lime-bright)}
.pbtn.active i{background:var(--white)}
.pbtn.active i::after{border-left-color:var(--brown)}

.h3{font-family:"Open Sans",sans-serif;font-weight:700;font-size:15px;color:#222;display:flex;align-items:center;gap:8px}
.list li{list-style:none;display:flex;gap:12px;font-size:11.5px;height:26px;align-items:center}
.dot{width:12px;height:12px;border-radius:50%;background:var(--lime);flex:none;position:relative}
.dot::after{content:"";position:absolute;left:3px;top:2px;width:4px;height:6px;border:solid var(--white);border-width:0 2px 2px 0;transform:rotate(45deg)}
.trip{display:flex;gap:10px;font-size:11.5px;width:280px}
.trip .thumb{width:24px;height:24px;flex:none;background:linear-gradient(135deg,#c89a6a,#7a5a3a)}
.bbtn{height:33px;background:var(--brown);border-radius:3px;color:var(--lime-bright);font-size:12px;display:flex;align-items:center;justify-content:center}

.badge{width:117px;height:40px;background:#efefef;border:1px solid #ddd;border-radius:2px}
.pager{display:flex;gap:4px}
.pager i{width:16px;height:16px;border-radius:50%;background:#999}
.pager i.on{background:var(--lime)}

/* sidebar */
.divider{left:789px;top:680px;width:1px;height:1360px;background:var(--line)}
.testi .avatar{width:50px;height:48px;background:linear-gradient(135deg,#b9c4cc,#7a8a95)}
.testi .name{font-family:"Open Sans",sans-serif;font-weight:700;font-size:14px;color:#222}
.testi .role{color:var(--green);font-size:12px}
.proposal{left:828px;top:1020px;width:243px;height:346px;background:var(--green);border-top:4px solid var(--green-dark)}
.proposal h3{position:absolute;left:14px;top:20px;font-family:"Open Sans",sans-serif;font-weight:600;font-size:21px;color:var(--white)}
.proposal .field{position:absolute;left:14px;width:215px;height:26px;background:var(--white);font-size:11px;color:#888;padding:5px 8px}
.proposal .send{position:absolute;left:14px;top:288px;width:104px;height:32px;background:var(--brown);border-radius:3px;color:var(--lime-bright);font-size:12px;display:flex;align-items:center;justify-content:center}
.tips li{list-style:none;display:flex;gap:10px;font-size:11.5px;padding:8px 0;border-bottom:1px solid var(--line);width:250px}
.card{background:var(--white);border:1px solid #bbb}
.photo{background:linear-gradient(135deg,#8a6a52,#3e2a1c)}

/* footer */
.footer{left:0;top:2062px;width:1200px;height:192px;background:linear-gradient(90deg,#2f9a36,#3aa33c 60%,#5cae3a)}
.footer .links{position:absolute;left:128px;top:42px;font-size:11.5px;color:var(--white);line-height:17px}
.footer h4{font-family:"Open Sans",sans-serif;font-weight:400;font-size:18px;color:var(--white)}
.footer .email{width:188px;height:26px;background:var(--white);font-size:11px;color:#888;padding:5px 8px}
.footer .sub{width:82px;height:32px;background:var(--brown);border-radius:3px;color:var(--lime-bright);font-size:12px;display:flex;align-items:center;justify-content:center}
.footer .fmark{position:absolute;left:921px;top:55px;width:102px;height:102px;border-radius:50%;background:var(--white);border:6px solid var(--green-dark);display:flex;align-items:center;justify-content:center;font-family:"Open Sans",sans-serif;font-weight:700;font-size:13px;color:var(--green);text-align:center}
.legal{font-size:10.5px;color:#444;line-height:15px}
</style>
</head>
<body>

<header>
  <div class="abs hero" role="img" aria-label="Photograph of a green lakeside landscape in Guatemala"></div>
  <div class="abs hero-shade"></div>
  <div class="abs logo"><span>Moraby<br>Pathways</span></div>

  <div class="abs util">
    <div class="label">Social Sharing</div>
    <div class="social"><i></i><i></i><i></i><i></i><i></i></div>
    <div class="links">Login &nbsp;|&nbsp; Register &nbsp;|&nbsp; Site Map</div>
    <div class="search">Search</div>
  </div>

  <nav class="abs nav">
    <a>MISSION</a><a>PROGRAMS</a><a class="active">SOCIAL ENTERPRISE</a><a>PRODUCTS</a><a>TRAVEL &amp; CULTURE</a><a>SPEAKING CIRCUITS</a><a>CONTACT</a>
  </nav>

  <div class="abs slogan">Wander<br><span class="mid">Gather</span><br>Reach higher</div>
  <div class="abs cta">Come along the Journey
    <svg viewBox="0 0 22 22"><circle cx="11" cy="11" r="10" fill="#d6e23a"/><path d="M9 6l6 5-6 5z" fill="#5a2e12"/></svg>
  </div>

  <div class="abs arrow" style="left:74px;top:343px"></div>
  <div class="abs arrow" style="left:1097px;top:353px"></div>

  <div class="abs video">
    <div class="screen" role="img" aria-label="Video frame introducing Moraby Pathways and the Harvest 7 Coffee project"></div>
    <div class="player">
      <div class="bar"><i></i></div>
      <div class="play"></div>
      <div class="time">0:02 / 0:10</div>
      <div class="q">720p</div>
    </div>
  </div>
</header>

<div class="abs content-bg"></div>

<main>
  <div class="abs h2" style="left:129px;top:680px">About Moraby <span class="tag">Wander</span></div>
  <div class="abs rule" style="left:129px;top:714px;width:617px"></div>
  <p class="abs para" style="left:129px;top:732px;width:617px">Lorem ipsum dolor sit amet, consectetuer adipiscing elit. Aenean commodo ligula eget dolor. Aenean massa. Cum sociis natoque penatibus et magnis dis parturient montes, nascetur ridiculus mus.</p>

  <div class="abs tile active" style="left:129px;top:788px">
    <svg viewBox="0 0 40 40"><path d="M6 18L34 6 24 34 19 22z" fill="none" stroke="#fff" stroke-width="2.5" stroke-linejoin="round"/></svg>
    Our Mission and<br>Philosophy
  </div>
  <div class="abs tile" style="left:285px;top:788px">
    <svg viewBox="0 0 40 40"><rect x="6" y="8" width="26" height="26" rx="4" fill="none" stroke="#b9c81a" stroke-width="3"/><path d="M16 26l2-6 12-12 4 4-12 12z" fill="#b9c81a"/></svg>
    History
  </div>
  <div class="abs tile" style="left:440px;top:788px">
    <svg viewBox="0 0 40 40"><circle cx="14" cy="13" r="6" fill="#b9c81a"/><circle cx="27" cy="13" r="6" fill="#b9c81a"/><path d="M3 34c0-9 5-13 11-13s11 4 11 13z" fill="#b9c81a"/><path d="M18 34c0-9 4-13 9-13s10 4 10 13z" fill="#b9c81a"/></svg>
    Advisory Board
  </div>
  <div class="abs tile" style="left:597px;top:788px">
    <svg viewBox="0 0 40 40"><path d="M10 30a8 8 0 010-16 10 10 0 0119-2 8 8 0 012 18z" fill="#b9c81a"/></svg>
    From the Founder
  </div>

  <div class="abs bul" style="left:133px;top:962px"><svg viewBox="0 0 16 16"><circle cx="8" cy="8" r="7" fill="#2e9b3a"/><circle cx="8" cy="8" r="2.5" fill="#fff"/></svg><span>Because we believe that the best way to unlock your unique gifts and potential is by helping others unlock theirs.</span></div>
  <div class="abs bul" style="left:133px;top:1012px"><svg viewBox="0 0 16 16"><circle cx="8" cy="8" r="7" fill="#2e9b3a"/><circle cx="8" cy="8" r="2.5" fill="#fff"/></svg><span>Moraby Pathways is a social enterprise that utilizes social entrepreneurship principles and systems in order to "unlock" people's human potential in ways that support themselves, their families, and initiates positive social change.</span></div>
  <div class="abs bul" style="left:133px;top:1082px"><svg viewBox="0 0 16 16"><circle cx="8" cy="8" r="7" fill="#2e9b3a"/><circle cx="8" cy="8" r="2.5" fill="#fff"/></svg><span>Moraby Pathways organizes and leads expeditions to Guatemala in order to unlock human potential for both participant and recipient.</span></div>

  <div class="abs h2" style="left:129px;top:1160px">Programs / Pricing <span class="tag">Gather</span></div>
  <div class="abs rule" style="left:129px;top:1194px;width:617px"></div>
  <p class="abs para" style="left:129px;top:1214px;width:617px">Lorem ipsum dolor sit amet, consectetuer adipiscing elit. Aenean commodo ligula eget dolor. Aenean massa. Cum sociis natoque penatibus et magnis dis parturient montes, nascetur ridiculus mus.</p>

  <div class="abs pbtn active" style="left:129px;top:1268px">Our Approach<i></i></div>
  <div class="abs pbtn" style="left:442px;top:1268px">Our Partners here and Abroad<i></i></div>
  <div class="abs pbtn" style="left:129px;top:1313px">Themed Trips<i></i></div>
  <div class="abs pbtn" style="left:442px;top:1313px">Pricing and Sample Trips<i></i></div>
  <div class="abs pbtn" style="left:129px;top:1357px">Past Trips Summaries<i></i></div>
  <div class="abs pbtn" style="left:442px;top:1357px">The $5 Quest<i></i></div>

  <div class="abs h2" style="left:129px;top:1452px">Benefits <span class="tag">Reach higher</span></div>
  <div class="abs rule" style="left:129px;top:1486px;width:617px"></div>

  <div class="abs h3" style="left:129px;top:1518px">
    <svg width="22" height="20" viewBox="0 0 22 20"><path d="M1 2h4l3 11h11l2-8H7" fill="none" stroke="#222" stroke-width="2"/><circle cx="9" cy="17" r="2" fill="#222"/><circle cx="18" cy="17" r="2" fill="#222"/></svg>
    Online Store
  </div>
  <ul class="abs list" style="left:129px;top:1558px">
    <li><span class="dot"></span>Aenean commodo ligula Lorem ipsum</li>
    <li><span class="dot"></span>Cum sociis natoque penatibus et magnis</li>
    <li><span class="dot"></span>Lorem ipsum dolor sit amet, consectetuer</li>
    <li><span class="dot"></span>Cum sociis natoque penatibus</li>
    <li><span class="dot"></span>Lorem ipsum dolor sit amet, consectetuer</li>
    <li><span class="dot"></span>Cum sociis natoque penatibus</li>
  </ul>
  <div class="abs" style="left:420px;top:1520px;width:1px;height:200px;background:var(--line)"></div>

  <div class="abs h3" style="left:466px;top:1518px">
    <svg width="22" height="18" viewBox="0 0 22 18"><rect x="1" y="4" width="20" height="13" rx="2" fill="#222"/><rect x="7" y="1" width="8" height="4" fill="#222"/><circle cx="11" cy="10.5" r="4" fill="#fff"/></svg>
    Past Trips
  </div>
  <div class="abs trip" style="left:468px;top:1560px"><span class="thumb"></span><span><b>Aenean commodo</b> ligula Lorem ipsum dolor - <b>More</b> | 13 June 2012</span></div>
  <div class="abs trip" style="left:468px;top:1604px"><span class="thumb"></span><span><b>Cum sociis natoque</b> penatibus et magnis dis parturient montes - <b>More</b> | 13 June 2012</span></div>
  <div class="abs trip" style="left:468px;top:1648px"><span class="thumb"></span><span><b>Lorem ipsum</b> dolor sit amet, consectetuer adipiscing elit. - <b>More</b> | 13 June 2012</span></div>
  <div class="abs bbtn" style="left:468px;top:1692px;width:130px">Contact Our Team</div>
  <div class="abs bbtn" style="left:603px;top:1692px;width:141px">Request a Proposal</div>

  <div class="abs h2" style="left:129px;top:1774px">Partners</div>
  <div class="abs rule" style="left:129px;top:1808px;width:617px"></div>
  <div class="abs h3" style="left:129px;top:1836px">Partners in Guatemala</div>
  <div class="abs pager" style="left:708px;top:1838px"><i></i><i class="on"></i></div>
  <div class="abs" style="left:129px;top:1868px;display:flex;gap:9px"><span class="badge"></span><span class="badge"></span><span class="badge"></span><span class="badge"></span><span class="badge"></span></div>
  <div class="abs h3" style="left:129px;top:1946px">Our Partners Abroad</div>
  <div class="abs pager" style="left:708px;top:1948px"><i></i><i class="on"></i></div>
  <div class="abs" style="left:129px;top:1978px;display:flex;gap:9px"><span class="badge"></span><span class="badge"></span><span class="badge"></span><span class="badge"></span><span class="badge"></span></div>

  <div class="abs divider"></div>

  <aside>
    <div class="abs h2 side" style="left:828px;top:680px">Moraby Testimonials</div>
    <div class="abs rule" style="left:828px;top:714px;width:243px"></div>

    <div class="abs testi" style="left:828px;top:740px;width:243px">
      <div style="display:flex;gap:12px;align-items:center"><div class="avatar" role="img" aria-label="Portrait photo"></div><div><div class="name">Marta Quill</div><div class="role">Advisor - Australia</div></div></div>
      <p style="margin-top:14px;font-size:11.5px">Lorem ipsum dolor sit amet, consectetuer adipiscing elit. Aenean commodo ligula eget dolor. Aenean massa.</p>
    </div>
    <div class="abs testi" style="left:828px;top:866px;width:243px">
      <div style="display:flex;gap:12px;align-items:center"><div class="avatar" role="img" aria-label="Portrait photo"></div><div><div class="name">Tomas Rell</div><div class="role">Advisor - Australia</div></div></div>
      <p style="margin-top:14px;font-size:11.5px">Cum sociis natoque penatibus et magnis dis parturient montes, nascetur ridiculus mus. Donec quam felis, ultricies nec</p>
    </div>

    <form class="abs proposal">
      <h3>Request a Proposal</h3>
      <div class="field" style="top:90px">Your Name</div>
      <div class="field" style="top:124px">Enter Email</div>
      <div class="field" style="top:161px;height:111px">Message</div>
      <div class="send">Send Request</div>
    </form>

    <div class="abs h2 side" style="left:828px;top:1409px">Moraby Travel Tips</div>
    <div class="abs rule" style="left:828px;top:1443px;width:243px"></div>
    <ul class="abs tips" style="left:828px;top:1466px">
      <li><span class="dot"></span>Cum sociis natoque penatibus et magnis</li>
      <li><span class="dot"></span>Cum sociis natoque penatibus et magnis dis parturient montes.</li>
      <li><span class="dot"></span>Cum sociis natoque penatibus et magnis</li>
    </ul>

    <div class="abs h2 side" style="left:828px;top:1614px">Moraby Business</div>
    <div class="abs rule" style="left:828px;top:1648px;width:243px"></div>
    <div class="abs h3" style="left:828px;top:1673px;font-size:13px">Business Card</div>
    <div class="abs" style="left:828px;top:1703px;font-size:11px">Front Side</div>
    <div class="abs" style="left:977px;top:1703px;font-size:11px">Back Side</div>
    <div class="abs card" style="left:828px;top:1723px;width:141px;height:80px" role="img" aria-label="Business card front design"></div>
    <div class="abs card" style="left:977px;top:1723px;width:94px;height:163px;background:linear-gradient(180deg,#fff 55%,#5a2e12 55%,#5a2e12 66%,#fff 66%)" role="img" aria-label="Business card back design"></div>
    <div class="abs h3" style="left:828px;top:1889px;font-size:13px">Our Pamphlet</div>
    <div class="abs photo" style="left:828px;top:1916px;width:115px;height:102px" role="img" aria-label="Photo of a child in Guatemala"></div>
    <div class="abs photo" style="left:946px;top:1916px;width:125px;height:102px;background:linear-gradient(135deg,#6a8a3a,#8a2a1a)" role="img" aria-label="Photo of coffee cherries on the branch"></div>
  </aside>
</main>

<footer>
  <div class="abs footer">
    <div class="links">Mission<br>Programs<br>Social Enterprise<br>Products<br>Travel &amp; Culture<br>Speaking Circuits<br>Contact</div>
    <h4 class="abs" style="left:314px;top:38px">Newsletter Signup</h4>
    <div class="abs email" style="left:314px;top:93px">Enter Email</div>
    <div class="abs sub" style="left:314px;top:127px">Subscribe</div>
    <h4 class="abs" style="left:578px;top:38px">Guatemala Profile</h4>
    <p class="abs" style="left:580px;top:86px;width:210px;font-size:11.5px;color:#fff">Lorem ipsum dolor sit amet, consectetuer adipiscing elit. Aenean commodo ligula eget dolor. Aenean massa. Cum sociis natoque</p>
    <div class="fmark">Moraby<br>Pathways</div>
  </div>
  <div class="abs legal" style="left:128px;top:2270px">All Right Reserve Copyright © 2012<br>With Moraby Pathways</div>
  <div class="abs legal" style="left:871px;top:2270px;width:200px;text-align:right">Privacy Policy | Terms of Use<br>Powered By : Larkfield Studio</div>
</footer>

</body>
</html>
```